A Leisure SPA Plaza Hotel needs Creative VIP Cards Design

We need VIP Cards Design for a SPA Plaza Hotel, This leisure SPA plaza hotel have multiple sub projects, such as leisure hotel room, large buffet restaurant, swimming pool, theatrical performances, sauna bath, massage, SPA, Tea bar, 3D cinema, KTV rooms, chess room, Internet cafes , art appreciation, children's Castle, Korean geothermal, table tennis, billiard room, GYM and other entertainments.
We need Three creative VIP Card design for 3 different level:
1. Golden Card
2. Platinum Card
3. Diamond Card
Attached, Please find the LOGO file and some sample, we new design with much better look than those samples.

```html
<!DOCTYPE html>
<html lang="en">
<head>
<meta charset="utf-8">
<title>Sunreef Leisure Plaza – VIP Member Cards</title>
<link href="https://fonts.googleapis.com/css2?family=Playfair+Display:wght@400;500&family=Josefin+Sans:wght@400;600&family=Noto+Sans+TC:wght@400;500&family=Yellowtail&display=swap" rel="stylesheet">
<style>
  :root {
    --page: #ffffff;
    --card-dark: #1f1a18;
    --card-mid: #2e2825;
    --text-light: #e9e4dc;
    --sig-ink: #1a1411;
    --gold-hi: #f1dc8a;
    --gold-mid: #c9a94e;
    --gold-lo: #8a6a24;
    --silver-hi: #f4f5f7;
    --silver-mid: #b9bcc2;
    --silver-lo: #6f7379;
    --steel-hi: #eef2f6;
    --steel-mid: #9fb0c2;
    --steel-lo: #5f7082;
    --plat-hi: #f0f3f7;
    --plat-mid: #a9b4c1;
    --plat-lo: #66707c;
  }
  * { box-sizing: border-box; margin: 0; padding: 0; }
  html, body { width: 1000px; height: 1200px; overflow: hidden; background: var(--page); }
  body { position: relative; font-family: "Josefin Sans", sans-serif; }

  .card {
    position: absolute; width: 385px; height: 240px; border-radius: 18px; overflow: hidden;
    background: radial-gradient(ellipse at 35% 30%, var(--card-mid), var(--card-dark) 70%);
  }
  .card--gold     { --hi: var(--gold-hi);   --mid: var(--gold-mid);   --lo: var(--gold-lo); }
  .card--silver   { --hi: var(--silver-hi); --mid: var(--silver-mid); --lo: var(--silver-lo); }
  .card--steel    { --hi: var(--steel-hi);  --mid: var(--steel-mid);  --lo: var(--steel-lo); }
  .card--platinum { --hi: var(--plat-hi);   --mid: var(--plat-mid);   --lo: var(--plat-lo); }

  /* soft placeholder for the flowing line ornament */
  .card__ornament {
    position: absolute; left: 0; bottom: 0; width: 100%; height: 90px;
    background:
      radial-gradient(ellipse 70% 60% at 45% 100%, color-mix(in srgb, var(--mid) 38%, transparent), transparent 75%);
  }
  .back .card__ornament { height: 70px; }

  .card__strip {
    position: absolute; top: 0; right: 0; width: 38px; height: 100%;
    background: linear-gradient(90deg, var(--lo), var(--hi) 45%, var(--mid) 75%, var(--lo));
  }

  .brand { position: absolute; left: 16px; top: 30px; width: 170px; text-align: center; color: var(--mid); }
  .brand__dot { display: block; width: 34px; height: 34px; margin: 0 auto 8px; border-radius: 50%; background: var(--mid); }
  .brand__zh { font-family: "Noto Sans TC", sans-serif; font-weight: 500; font-size: 19px; letter-spacing: 1px; }
  .brand__en { font-family: "Noto Sans TC", sans-serif; font-weight: 500; font-size: 11px; margin-top: 2px; }

  .tier { position: absolute; left: 196px; top: 14px; width: 140px; text-align: center; color: var(--mid); }
  .tier__stars { font-size: 11px; letter-spacing: 2px; line-height: 1; }
  .tier__vip {
    font-family: "Playfair Display", serif; font-size: 62px; line-height: 1; letter-spacing: 1px;
    background: linear-gradient(180deg, var(--hi), var(--mid) 55%, var(--lo));
    -webkit-background-clip: text; background-clip: text; color: transparent;
  }
  .tier__label { font-size: 10px; letter-spacing: 4px; margin-top: 4px; }
  .tier__zh { font-family: "Noto Sans TC", sans-serif; font-size: 12px; color: var(--text-light); margin-top: 4px; }

  .back { text-align: center; color: var(--text-light); }
  .back__en { position: absolute; left: 0; width: 100%; font-size: 7.5px; letter-spacing: 0.6px; line-height: 1.25; font-weight: 600; }
  .back__zh { position: absolute; left: 0; width: 100%; font-family: "Noto Sans TC", sans-serif; font-size: 12px; line-height: 1.3; }
  .back__sig {
    position: absolute; left: 48px; top: 122px; width: 290px; height: 40px; border-radius: 6px;
    background: linear-gradient(90deg, var(--lo), var(--hi) 50%, var(--mid));
    font-family: "Yellowtail", "Brush Script MT", cursive; font-size: 24px; line-height: 40px; color: var(--sig-ink);
  }
</style>
</head>
<body>

<article class="card card--gold" style="left:98px;top:28px">
  <div class="card__ornament" role="img" aria-label="Flowing metallic gold line ornament"></div>
  <div class="card__strip"></div>
  <div class="brand"><span class="brand__dot"></span><div class="brand__zh">日礁休闲广场</div><div class="brand__en">Sunreef Leisure Plaza</div></div>
  <div class="tier"><div class="tier__stars">★ ★ ★</div><div class="tier__vip">VIP</div><div class="tier__label">MEMBER CARD</div><div class="tier__zh">會員卡</div></div>
</article>

<article class="card card--gold back" style="left:510px;top:28px">
  <div class="card__ornament" role="img" aria-label="Flowing metallic gold line ornament"></div>
  <p class="back__en" style="top:24px">PLEASE SHOW YOUR MEMBERSHIP CARD WHEN YOU CHECK OUT</p>
  <p class="back__zh" style="top:35px">請出示您的會員卡當您簽出</p>
  <p class="back__en" style="top:57px">SIGNATURE AND USE OF THIS CARD CONFIRM THE<br>ACCEPTANCE OF THE TERMS AND CONDITIONS OF MEMBERSHIP</p>
  <p class="back__zh" style="top:80px">簽名並使用此卡確認了<br>接受本條款和會員資格條件的</p>
  <div class="back__sig">Leo Marston</div>
  <p class="back__en" style="top:171px">AUTHORIZED SIGNATURE</p>
  <p class="back__zh" style="top:182px">授權簽名</p>
</article>

<article class="card card--silver" style="left:98px;top:305px">
  <div class="card__ornament" role="img" aria-label="Flowing metallic silver line ornament"></div>
  <div class="card__strip"></div>
  <div class="brand"><span class="brand__dot"></span><div class="brand__zh">日礁休闲广场</div><div class="brand__en">Sunreef Leisure Plaza</div></div>
  <div class="tier"><div class="tier__stars">★ ★ ★</div><div class="tier__vip">VIP</div><div class="tier__label">MEMBER CARD</div><div class="tier__zh">會員卡</div></div>
</article>

<article class="card card--steel" style="left:506px;top:305px">
  <div class="card__ornament" role="img" aria-label="Flowing metallic steel-blue line ornament"></div>
  <div class="card__strip"></div>
  <div class="brand"><span class="brand__dot"></span><div class="brand__zh">日礁休闲广场</div><div class="brand__en">Sunreef Leisure Plaza</div></div>
  <div class="tier"><div class="tier__stars">★ ★ ★</div><div class="tier__vip">VIP</div><div class="tier__label">MEMBER CARD</div><div class="tier__zh">會員卡</div></div>
</article>

<article class="card card--platinum" style="left:303px;top:570px">
  <div class="card__ornament" role="img" aria-label="Flowing metallic platinum line ornament"></div>
  <div class="card__strip"></div>
  <div class="brand"><span class="brand__dot"></span><div class="brand__zh">日礁休闲广场</div><div class="brand__en">Sunreef Leisure Plaza</div></div>
  <div class="tier"><div class="tier__stars">★ ★ ★</div><div class="tier__vip">VIP</div><div class="tier__label">MEMBER CARD</div><div class="tier__zh">會員卡</div></div>
</article>

</body>
</html>
```